Banner ad for hyper local news site

We need a banner (that we will use on our own site) to explain to people that they can "be the reporter" in their local area. Lanternpost is an Australia community news network. We cover local news on a daily basis but also allow people and organisations to publish their own news direct to the site. We are trying to encourage local dialogue and to empower people to talk about the things that matter to them and get their issues on the news agenda.

We need a 'call to action' banner that explains to our users that they can post their own stories on the site.

Some suggested text (thinking this would be rolling)

*Lanternpost is YOUR voice in the community
*You can 'be the reporter' and write your own news
*To be heard, contribute your stories, click here - it's free

The banner doesn't have to be slick - we'd prefer a warm and friendly community feeling....but also something in keeping with the look and feel of our site wwww.lanternpost-example.com.au

Industry/Entity Type

News

```html
<!DOCTYPE html>
<html lang="en">
<head>
<meta charset="utf-8">
<title>Lanternpost – Be a Reporter banner concepts</title>
<link href="https://fonts.googleapis.com/css2?family=Open+Sans:ital,wght@0,700;0,800;1,700;1,800&family=Delius&display=swap" rel="stylesheet">
<style>
  :root {
    --stripe-light: #ffffff;
    --stripe-blue: #e6f3fa;
    --sheet: #ffffff;
    --sheet-edge: #c9d2d8;
    --banner-navy: #0e3a6c;
    --street-mid: #3f6b98;
    --street-light: #7a98b8;
    --headline: #ffffff;
    --accent-green: #7fd424;
    --accent-dark: #123a12;
    --note-ink: #4a4a4a;
  }
  * { margin: 0; padding: 0; box-sizing: border-box; }
  html, body { width: 1200px; height: 900px; overflow: hidden; }
  body {
    position: relative;
    background: repeating-linear-gradient(90deg, var(--stripe-light) 0 6px, var(--stripe-blue) 6px 12px);
  }
  .presentation-sheet {
    position: absolute;
    left: 250px; top: 0;
    width: 674px; height: 900px;
    background: var(--sheet);
    box-shadow: 0 0 6px 1px var(--sheet-edge);
  }
  .banner {
    position: absolute;
    left: 136px;
    width: 936px; height: 120px;
    background: var(--banner-navy);
    overflow: hidden;
    font-family: "Open Sans", sans-serif;
  }
  .banner--news { top: 74px; }
  .banner--voice { top: 352px; }
  .banner--stories { top: 652px; }
  .street-photo {
    position: absolute;
    left: 200px; top: 0; right: 0; bottom: 0;
    background: linear-gradient(90deg, var(--banner-navy) 0%, var(--street-mid) 45%, var(--street-light) 75%, var(--street-mid) 100%);
    opacity: 0.85;
  }
  .brand {
    position: absolute;
    left: 14px; top: 38px;
    display: flex; align-items: center; gap: 6px;
  }
  .brand-name {
    color: var(--headline);
    font-weight: 800;
    font-size: 30px;
    letter-spacing: -0.5px;
  }
  .brand-dot {
    width: 16px; height: 16px;
    border-radius: 50%;
    background: var(--accent-green);
    align-self: flex-start;
    margin-top: -10px;
  }
  .headline {
    position: absolute;
    right: 36px; top: 4px;
    text-align: right;
    color: var(--headline);
    text-shadow: 0 1px 3px rgba(0,0,0,0.45);
  }
  .headline-invite {
    font-size: 31px; font-weight: 700; line-height: 40px;
  }
  .headline-invite em { font-weight: 800; }
  .headline-action {
    font-size: 50px; font-weight: 700; line-height: 64px;
    letter-spacing: -0.5px;
  }
  .headline-action em {
    color: var(--accent-green);
    font-weight: 800;
    text-shadow: 0 0 2px var(--accent-dark), 0 1px 3px rgba(0,0,0,0.5);
  }
  .design-note {
    position: absolute;
    left: 276px;
    font-family: "Delius", cursive;
    font-size: 19.5px;
    line-height: 30px;
    color: var(--note-ink);
  }
  .design-note--news { top: 212px; }
  .design-note--voice { top: 480px; }
  .design-note--stories { top: 780px; }
</style>
</head>
<body>
  <div class="presentation-sheet"></div>

  <section class="banner banner--news">
    <div class="street-photo" role="img" aria-label="Photo of a local street corner with shopfronts, tinted blue"></div>
    <div class="brand"><span class="brand-name">Lanternpost</span><span class="brand-dot"></span></div>
    <div class="headline">
      <p class="headline-invite">Be a Reporter on your <em>Lanternpost!</em></p>
      <p class="headline-action">...Report the <em>NEWS</em></p>
    </div>
  </section>
  <p class="design-note design-note--news">3key messages - users will not remember more than that<br>small green dot travels around (animated)&nbsp; perimeter<br>shape of logo - catches the eye!</p>

  <section class="banner banner--voice">
    <div class="street-photo" role="img" aria-label="Photo of a local street corner with shopfronts, tinted blue"></div>
    <div class="brand"><span class="brand-name">Lanternpost</span><span class="brand-dot"></span></div>
    <div class="headline">
      <p class="headline-invite">Be a Reporter on your <em>Lanternpost!</em></p>
      <p class="headline-action">...Share your <em>VOICE</em></p>
    </div>
  </section>
  <p class="design-note design-note--voice">Animated Flash Banner with crossfade transitions<br>between the key messages on bottom of banner.&nbsp; Top<br>line of text remains the same.</p>

  <section class="banner banner--stories">
    <div class="street-photo" role="img" aria-label="Photo of a local street corner with shopfronts, tinted blue"></div>
    <div class="brand"><span class="brand-name">Lanternpost</span><span class="brand-dot"></span></div>
    <div class="headline">
      <p class="headline-invite">Be a Reporter on your <em>Lanternpost!</em></p>
      <p class="headline-action">...Tell your <em>STORIES</em></p>
    </div>
  </section>
  <p class="design-note design-note--stories">A simple effective design when running on the page - not a<br>deterent or distraction to users is not annoying but<br>catches the eye of the user.</p>
</body>
</html>
```